New Zealand Export company needs business cards

We need new business cards to match our new logo for a company based in New Zealand who deal specifically with the Pacific Islands. We source, consolidate and ship products out of New Zealand to the Pacific Islands. Will attach our old ones and also new logo.
Would like the Islands we deal with and the areas of work we have access to, to be included on the business cards.

Contact Information for Business Card

T +64 9 571 3048
F +64 9 571 6285
12-18 Kowhai Lane, Drury, 2113
PO Box 814, Drury, Auckland 2247, New Zealand
www.falconfreight.example.nz
E sales@falconfreight.example.nz

Font styles to use
Sans Serif

Colors
85abd2
33a6d7
ffffff

Requirements
Must have
• A company of PWM

```html
<!DOCTYPE html>
<html lang="en">
<head>
<meta charset="utf-8">
<title>Falcon Freight – Business Cards</title>
<link rel="stylesheet" href="https://fonts.googleapis.com/css2?family=Roboto:wght@400;500;700;900&display=swap">
<style>
  :root {
    --bg: #2b2e33;
    --card-white: #ffffff;
    --brand-dark: #1559a8;
    --brand-light: #3cbfea;
    --text-grey: #3d3d3d;
    --sky: #3f7fd6;
    --cloud: #cfe0f2;
    --lagoon: #2ec9cf;
    --lagoon-deep: #2aa9c2;
  }
  * { box-sizing: border-box; margin: 0; padding: 0; }
  html, body {
    width: 1200px; height: 1000px; overflow: hidden;
    background: var(--bg);
    font-family: "Roboto", sans-serif;
  }
  .canvas { position: relative; width: 1200px; height: 1000px; }
  .card {
    position: absolute; left: 210px; width: 780px; height: 440px;
    border-radius: 24px; overflow: hidden;
    box-shadow: 0 12px 30px rgba(0,0,0,0.45);
  }
  .card--front { top: 45px; }
  .card--back { top: 515px; background: var(--card-white); }

  .scene-photo {
    position: absolute; inset: 0;
    background: linear-gradient(180deg,
      var(--sky) 0%, var(--cloud) 30%, #9cc3e6 42%,
      #3f7a4a 48%, #2e8a63 54%, var(--lagoon) 60%, var(--lagoon-deep) 100%);
  }
  .brand {
    position: absolute; display: flex; align-items: center; gap: 14px;
    font-weight: 900; letter-spacing: 2px; text-transform: uppercase;
  }
  .brand__square { width: 44px; height: 44px; }
  .card--front .brand { left: 70px; top: 250px; color: var(--card-white); font-size: 44px; }
  .card--front .brand__square { background: var(--card-white); }

  .card--back .brand { left: 55px; top: 150px; color: var(--brand-dark); font-size: 36px; }
  .card--back .brand__square { width: 38px; height: 38px; background: var(--brand-dark); }
  .parent-line {
    position: absolute; left: 55px; top: 212px;
    color: var(--brand-dark); font-size: 22px; font-weight: 400;
  }
  .parent-line strong { font-weight: 400; letter-spacing: 1px; }

  .divider {
    position: absolute; left: 440px; top: 140px; width: 2px; height: 160px;
    background: var(--brand-dark);
  }
  .contact {
    position: absolute; left: 468px; top: 132px;
    color: var(--text-grey); font-size: 17px; line-height: 1.3;
  }
  .contact__address { margin-bottom: 6px; }
  .contact__row { display: flex; align-items: center; gap: 10px; }
  .contact__row svg { width: 15px; height: 15px; flex: none; fill: var(--brand-dark); }

  .swoosh { position: absolute; left: 0; bottom: 0; width: 780px; height: 150px; }
</style>
</head>
<body>
<main class="canvas">

  <section class="card card--front">
    <div class="scene-photo" role="img" aria-label="Tropical Pacific island lagoon with turquoise water, palm trees on a small islet, green mountains and white clouds in a blue sky"></div>
    <div class="brand"><span class="brand__square"></span>Falcon Freight</div>
  </section>

  <section class="card card--back">
    <div class="brand"><span class="brand__square"></span>Falcon Freight</div>
    <p class="parent-line">A company of <strong>PWM</strong></p>

    <div class="divider"></div>

    <div class="contact">
      <p class="contact__address">12-18 Kowhai Lane, Drury, 2113<br>PO Box 814, Drury, Auckland 2247,<br>New Zealand</p>
      <p class="contact__row">
        <svg viewBox="0 0 24 24" aria-hidden="true"><path d="M6.6 10.8a15 15 0 0 0 6.6 6.6l2.2-2.2c.3-.3.7-.4 1-.2 1.1.4 2.3.6 3.6.6.6 0 1 .4 1 1V20c0 .6-.4 1-1 1A17 17 0 0 1 3 4c0-.6.4-1 1-1h3.5c.6 0 1 .4 1 1 0 1.3.2 2.5.6 3.6.1.3 0 .7-.2 1z"/></svg>
        +64 9 571 3048</p>
      <p class="contact__row">
        <svg viewBox="0 0 24 24" aria-hidden="true"><path d="M6 2h12v5H6zM4 8h16a2 2 0 0 1 2 2v7h-4v5H6v-5H2v-7a2 2 0 0 1 2-2zm4 9v3h8v-3z"/></svg>
        +64 9 571 6285</p>
      <p class="contact__row">
        <svg viewBox="0 0 24 24" aria-hidden="true"><path d="M2 5h20v14H2zm2 2v.5l8 5 8-5V7z"/></svg>
        E sales@falconfreight.example.nz</p>
      <p class="contact__row">
        <svg viewBox="0 0 24 24" aria-hidden="true"><circle cx="12" cy="12" r="10"/></svg>
        www.falconfreight.example.nz</p>
    </div>

    <svg class="swoosh" viewBox="0 0 780 150" preserveAspectRatio="none" aria-hidden="true">
      <path d="M0 20 C 250 110, 520 150, 780 130 L780 150 L0 150 Z" fill="var(--brand-dark)"/>
      <path d="M40 18 C 280 100, 540 132, 760 118" fill="none" stroke="var(--brand-light)" stroke-width="4"/>
    </svg>
  </section>

</main>
</body>
</html>
```